Business card por a urban DJ, up scale audience target

Need a sober design, modern, conservative colors but i can consider some options, y play rnb, hip hop, EDM and top40.

Business card for contact and personal info, double sided, use logo attrached please; im 42 so i need a card acording to my age an target audience.

Target Market(s)

Adult people, up scale audience

Industry/Entity Type

Music Download

Contact Information for Business Card

Cel (574) 3209415586 www.lumaverso.com

Requirements
Must have
• open mind
Nice to have
• open mind
Should not have
• DJ

```html
<!DOCTYPE html>
<html lang="en">
<head>
<meta charset="utf-8">
<title>Lumaverso business card</title>
<link rel="stylesheet" href="https://fonts.googleapis.com/css2?family=Open+Sans:wght@400;700;800&display=swap">
<style>
  :root {
    --backdrop: #111111;
    --card: #1c1c1c;
    --ink: #ffffff;
    --ink-soft: #e6e6e6;
  }
  * { margin: 0; padding: 0; box-sizing: border-box; }
  html, body {
    width: 1200px;
    height: 720px;
    overflow: hidden;
    background: var(--backdrop);
  }
  .canvas {
    width: 1200px;
    height: 720px;
    display: flex;
    align-items: center;
    justify-content: center;
  }
  .business-card {
    width: 840px;
    height: 480px;
    background: var(--card);
    display: flex;
    flex-direction: column;
    align-items: center;
    justify-content: center;
    font-family: "Open Sans", Arial, sans-serif;
    color: var(--ink);
  }
  .brand {
    display: flex;
    align-items: center;
    gap: 18px;
    margin-bottom: 34px;
  }
  .brand-square {
    width: 26px;
    height: 26px;
    background: var(--ink);
  }
  .brand-name {
    font-size: 92px;
    font-weight: 800;
    letter-spacing: 6px;
    line-height: 1;
  }
  .contact {
    display: flex;
    flex-direction: column;
    align-items: center;
    gap: 6px;
    font-size: 19px;
    color: var(--ink-soft);
  }
  .phone-icon {
    width: 22px;
    height: 22px;
    margin-bottom: 6px;
  }
  .website strong { font-weight: 700; color: var(--ink); }
</style>
</head>
<body>
  <main class="canvas">
    <section class="business-card">
      <div class="brand">
        <span class="brand-square"></span>
        <span class="brand-name">LUMA</span>
      </div>
      <div class="contact">
        <svg class="phone-icon" viewBox="0 0 22 22" aria-hidden="true">
          <rect x="0" y="0" width="22" height="22" rx="3" fill="#ffffff"/>
          <path d="M4 9 Q11 4 18 9 L16.5 11 L14 10 L14 8.5 Q11 7.5 8 8.5 L8 10 L5.5 11 Z" fill="#1c1c1c"/>
          <rect x="6" y="12" width="10" height="6" rx="1" fill="#1c1c1c"/>
        </svg>
        <span class="phone">(574) 3209415586</span>
        <span class="website">www.<strong>lumaverso</strong>.com</span>
      </div>
    </section>
  </main>
</body>
</html>
```